Flyer Design

I need a flyer as Iam starting a business which cleans Leather couches,sofas,chairs for residential and businesses.
We clean the interiors of automobiles and marine craft, boats large and small.
We would like to be able to get across the message that we are affordable, personal and reliable.
The Gold coast is our market and within this area there is a large amount of holiday apartments and houses which do experience high traffic to their living and dinning areas.

Target Market(s)

Target market Home,Apartment,Marine and Auto Owners

Industry/Entity Type

Residential

Requirements
Must have
• The flyer must have Company name which is BRIGHT HIDE CARE MOBILE NUMBER
0471932054
EMAIL marvtolk@quellnet.com
Colours would like bright Gold or green or Red eith black lettering very modern font
Nice to have
• I would like to keep it as simple and clean looking.but eye catching
Should not have
• Dont want the flyer to look like a Real Estate flyer or a pizza advertisement.

```html
<!DOCTYPE html>
<html lang="en">
<head>
<meta charset="utf-8">
<title>Bright Hide Care – Flyer</title>
<link href="https://fonts.googleapis.com/css2?family=Marcellus&family=Montserrat:wght@600&display=swap" rel="stylesheet">
<style>
  :root {
    --gold-deep: #b8871f;
    --gold-mid: #e2b94a;
    --gold-light: #fbeb9a;
    --red: #a51c2a;
    --red-dark: #7c111c;
    --red-photo: #c4202c;
    --cream-photo: #d9c6a6;
    --white: #ffffff;
    --ink: #1b1b1b;
  }
  html, body {
    margin: 0;
    padding: 0;
    width: 922px;
    height: 1200px;
    overflow: hidden;
    background: var(--white);
  }
  .flyer {
    display: block;
    width: 922px;
    height: 1200px;
  }
  .brand-title {
    font-family: "Marcellus", Georgia, serif;
    font-size: 66px;
    fill: var(--white);
    letter-spacing: 1px;
  }
  .service-main {
    font-family: "Marcellus", Georgia, serif;
    font-size: 23px;
    fill: var(--ink);
  }
  .service-sub {
    font-family: "Marcellus", Georgia, serif;
    font-size: 20px;
    fill: var(--ink);
  }
  .bullet { fill: var(--red); }
  .contact-text {
    font-family: "Montserrat", Arial, sans-serif;
    font-weight: 600;
    font-size: 30px;
    fill: var(--white);
  }
  .photo-ring { fill: none; stroke: var(--red); stroke-width: 6; }
  .icon-line { fill: none; stroke: var(--white); stroke-width: 2.5; }
</style>
</head>
<body>
<svg class="flyer" viewBox="0 0 922 1200" xmlns="http://www.w3.org/2000/svg">
  <defs>
    <linearGradient id="goldField" x1="0" y1="0" x2="1" y2="1">
      <stop offset="0" stop-color="var(--gold-deep)"/>
      <stop offset="0.35" stop-color="var(--gold-light)"/>
      <stop offset="0.6" stop-color="var(--gold-mid)"/>
      <stop offset="1" stop-color="var(--gold-deep)"/>
    </linearGradient>
    <linearGradient id="sofaTone" x1="0" y1="0" x2="0" y2="1">
      <stop offset="0" stop-color="#e0303a"/>
      <stop offset="1" stop-color="#8e0f18"/>
    </linearGradient>
  </defs>

  <!-- background field -->
  <rect class="gold-field" width="922" height="1200" fill="url(#goldField)"/>

  <!-- hero sofa -->
  <rect class="hero-sofa" x="135" y="55" width="635" height="300" rx="30" fill="url(#sofaTone)" role="img" aria-label="Photo of a glossy red three-seat leather sofa"/>

  <!-- white content panel -->
  <path class="content-panel" d="M0 470 L922 380 L922 520 C720 600 380 820 0 930 Z" fill="var(--white)"/>
  <path class="swoosh-line" d="M0 938 C380 830 720 610 922 528" fill="none" stroke="var(--red)" stroke-width="5"/>

  <!-- title band -->
  <path class="title-band" d="M0 388 L922 303 L922 382 L0 470 Z" fill="var(--red)"/>
  <text class="brand-title" x="118" y="452" transform="rotate(-5 118 452)" textLength="690" lengthAdjust="spacingAndGlyphs">BRIGHT HIDE CARE</text>

  <!-- services list -->
  <g class="services" transform="translate(97 548) rotate(-5)">
    <circle class="bullet" cx="0" cy="-7" r="6"/>
    <text class="service-main" x="20" y="0">LEATHER CLEANING FOR RESIDENTIAL AND BUSINESSES:</text>
    <circle class="bullet" cx="55" cy="29" r="4"/>
    <text class="service-sub" x="72" y="36">COUCHES</text>
    <circle class="bullet" cx="55" cy="64" r="4"/>
    <text class="service-sub" x="72" y="71">SOFAS</text>
    <circle class="bullet" cx="55" cy="99" r="4"/>
    <text class="service-sub" x="68" y="106">CHAIRS</text>
    <circle class="bullet" cx="0" cy="138" r="6"/>
    <text class="service-main" x="20" y="145">INTERIOR OF AUTOMOBILES</text>
    <circle class="bullet" cx="0" cy="173" r="6"/>
    <text class="service-main" x="20" y="180">INTERIOR OF MARINE CRAFT &amp; BOATS</text>
  </g>

  <!-- service photos -->
  <g class="service-photos">
    <circle cx="853" cy="545" r="66" fill="var(--cream-photo)" role="img" aria-label="Photo of beige leather car seats"/>
    <circle class="photo-ring" cx="853" cy="545" r="66"/>
    <circle cx="735" cy="690" r="82" fill="#cfc2a8" role="img" aria-label="Photo of a car seat being cleaned by hand"/>
    <circle class="photo-ring" cx="735" cy="690" r="82"/>
    <circle cx="541" cy="830" r="115" fill="var(--red-photo)" role="img" aria-label="Photo of a hand wiping a red leather couch"/>
    <circle class="photo-ring" cx="541" cy="830" r="115"/>
    <circle cx="280" cy="885" r="73" fill="#c9a27e" role="img" aria-label="Photo of a cream leather sofa with red cushions"/>
    <circle class="photo-ring" cx="280" cy="885" r="73"/>
    <circle cx="97" cy="925" r="63" fill="#bdb6aa" role="img" aria-label="Photo of a car seat being polished"/>
    <circle class="photo-ring" cx="97" cy="925" r="63"/>
  </g>

  <!-- contact ribbon -->
  <path class="contact-ribbon" d="M0 1075 L775 1028 L705 1200 L0 1200 Z" fill="var(--red)"/>
  <path class="ribbon-curl" d="M775 1028 L735 1075 Q745 1050 700 1065 Z" fill="var(--red-dark)"/>

  <g class="contact-phone">
    <rect class="icon-line" x="133" y="1080" width="18" height="28" rx="3"/>
    <line class="icon-line" x1="138" y1="1102" x2="146" y2="1102"/>
    <text class="contact-text" x="178" y="1107">0471932054</text>
  </g>
  <g class="contact-email">
    <rect class="icon-line" x="126" y="1135" width="34" height="24" rx="2"/>
    <polyline class="icon-line" points="126,1135 143,1150 160,1135"/>
    <text class="contact-text" x="178" y="1156">marvtolk@quellnet.com</text>
  </g>
</svg>
</body>
</html>
```